serious, thorough, light and simple - that's my advice and mediations

My business card should combine my logo (uploaded file) and my homepage (https://fellor-mediation.webnestsite.com).

Contact Information for Business Card

Name: Sabine Fellor di Vanti
Phone: 076 412 58 94
mail: sfellor@postkiv.ch
web: www.fellor-di-vanti.ch

```html
<!DOCTYPE html>
<html lang="de">
<head>
<meta charset="utf-8">
<title>Sabine Fellor di Vanti – Visitenkarte</title>
<link rel="stylesheet" href="https://fonts.googleapis.com/css2?family=Montserrat:wght@300;400;500&display=swap">
<style>
  :root {
    --backdrop: #ebe6de;
    --card-white: #ffffff;
    --navy-top: #1c4e70;
    --navy-bottom: #2a3d8c;
    --gold: #a8834f;
    --text-light: #ffffff;
    --shadow: rgba(60, 40, 20, 0.28);
  }
  html, body {
    margin: 0;
    padding: 0;
    width: 900px;
    height: 1200px;
    overflow: hidden;
    background: var(--backdrop);
    font-family: "Montserrat", sans-serif;
  }
  .canvas {
    position: relative;
    width: 900px;
    height: 1200px;
  }
  .card {
    position: absolute;
    left: 80px;
    width: 733px;
    height: 429px;
    border-radius: 22px;
    overflow: hidden;
    background: var(--card-white);
    box-shadow: 0 6px 18px var(--shadow);
  }
  .card--front { top: 128px; }
  .card--back { top: 646px; }

  .brand {
    position: absolute;
    text-align: center;
  }
  .brand__name {
    font-weight: 400;
    color: var(--gold);
    letter-spacing: 0.5px;
    white-space: nowrap;
    margin: 0;
  }
  .brand__ground {
    margin: 22px auto 0;
    height: 14px;
    border-radius: 50%;
    background: radial-gradient(ellipse at center, rgba(0,0,0,0.12) 0%, rgba(0,0,0,0) 70%);
  }
  .card--front .brand {
    left: 0;
    right: 0;
    top: 200px;
  }
  .card--front .brand__name { font-size: 44px; }
  .card--front .brand__ground { width: 260px; }

  .back-art {
    position: absolute;
    inset: 0;
  }
  .card--back .brand {
    left: 355px;
    width: 310px;
    top: 190px;
  }
  .card--back .brand__name { font-size: 34px; }
  .card--back .brand__ground { width: 200px; margin-top: 18px; }

  .holder-name {
    position: absolute;
    left: 44px;
    top: 52px;
    margin: 0;
    font-weight: 400;
    font-size: 19px;
    color: var(--text-light);
  }
  .contact-list {
    position: absolute;
    left: 44px;
    top: 290px;
    margin: 0;
    padding: 0;
    list-style: none;
  }
  .contact-list li {
    display: flex;
    align-items: center;
    height: 29px;
    font-size: 16.5px;
    font-weight: 400;
    color: var(--text-light);
  }
  .contact-icon {
    width: 22px;
    height: 22px;
    margin-right: 10px;
    flex: none;
  }
</style>
</head>
<body>
<main class="canvas">

  <section class="card card--front" aria-label="Vorderseite">
    <div class="brand">
      <p class="brand__name">Wege im Dialog</p>
      <div class="brand__ground"></div>
    </div>
  </section>

  <section class="card card--back" aria-label="Rückseite">
    <svg class="back-art" width="733" height="429" viewBox="0 0 733 429" aria-hidden="true">
      <defs>
        <linearGradient id="navyPanel" x1="0" y1="0" x2="0" y2="1">
          <stop offset="0" stop-color="var(--navy-top)"/>
          <stop offset="1" stop-color="var(--navy-bottom)"/>
        </linearGradient>
      </defs>
      <rect width="733" height="429" fill="url(#navyPanel)"/>
      <rect x="510" y="0" width="223" height="429" fill="var(--card-white)"/>
      <circle cx="510" cy="214" r="236" fill="var(--card-white)"/>
    </svg>

    <p class="holder-name">Sabine Fellor di Vanti</p>

    <ul class="contact-list">
      <li>
        <svg class="contact-icon" viewBox="0 0 22 22" aria-hidden="true">
          <circle cx="11" cy="11" r="10" fill="none" stroke="#ffffff" stroke-opacity="0.6" stroke-width="1"/>
          <path d="M7.5 6.5l2 -0.5 1.2 2.6 -1.3 1a6 6 0 0 0 3 3l1 -1.3 2.6 1.2 -0.5 2c-4.5 0.3 -8.3 -3.5 -8 -8z" fill="#d9a35a"/>
        </svg>
        076 412 58 94
      </li>
      <li>
        <svg class="contact-icon" viewBox="0 0 22 22" aria-hidden="true">
          <circle cx="11" cy="11" r="10" fill="none" stroke="#ffffff" stroke-opacity="0.6" stroke-width="1"/>
          <rect x="6" y="7.5" width="10" height="7" fill="#d9a35a"/>
          <path d="M6 7.5l5 4 5 -4" fill="none" stroke="#2a3d8c" stroke-width="1"/>
        </svg>
        sfellor@postkiv.ch
      </li>
      <li>
        <svg class="contact-icon" viewBox="0 0 22 22" aria-hidden="true">
          <circle cx="11" cy="11" r="10" fill="none" stroke="#ffffff" stroke-opacity="0.6" stroke-width="1"/>
          <circle cx="11" cy="11" r="5" fill="none" stroke="#d9a35a" stroke-width="1.2"/>
          <ellipse cx="11" cy="11" rx="2.2" ry="5" fill="none" stroke="#d9a35a" stroke-width="1"/>
          <line x1="6" y1="11" x2="16" y2="11" stroke="#d9a35a" stroke-width="1"/>
        </svg>
        www.fellor-di-vanti.ch
      </li>
    </ul>

    <div class="brand">
      <p class="brand__name">Wege im Dialog</p>
      <div class="brand__ground"></div>
    </div>
  </section>

</main>
</body>
</html>
```